Business Card Design - front and back

Residential real estate agent looking for a an emphasis on my first name (last name is hard to spell).  Would love the slogan "Every key opens a new chapter" on the card.  Simple, easy to read business card that makes people want to pick it up and remember it.  The Bright Lantern Realty has to be on the front of card but does not need to be the emphasis.  Prefer locations on the back.  Would love a home on it.  Looking for simply elegant in the card that shows I am a non-complicated, warm, honest real estate agent.
NEED ONE OF MY PICTURES ON THE CARD.  LEAVING WHICH ONE UP TO THE DESIGNER.

Industry/Entity Type
Real Estate
Contact Information for Business Card
Gloria Penwick, Broker Associate, Bright Lantern Realty, 727-481-6054 cell, hereisgloria@maplenest.example, listedbygloria.example, Bright Lantern Realty locations: 48217 Orrington Blvd Ste 101, Tampa, FL  30918, 2948 Velo Ct Ste 101, New Port Richey, FL  30742
I NEED THIS DOUBLE SIDED - THE SELECTION BELOW WILL NOT ALLOW IT?
Requirements
Must have
- Emphasis on my first name
a home in it
LOVE Marla dobrin's logo which sits on the left side in the margin at
http://marladobrin.quillagentsite.example/
Something with that idea is exactly what I am looking for.
Nice to have
- Nice script that is readable.
Should not have
- I am looking for something simple

```html
<!DOCTYPE html>
<html lang="en">
<head>
<meta charset="utf-8">
<title>Bright Lantern Realty – Gloria Penwick Business Card</title>
<link href="https://fonts.googleapis.com/css2?family=Open+Sans:wght@700&family=Cabin:wght@400&family=Allura&display=swap" rel="stylesheet">
<style>
  :root {
    --stage: #5e5e5e;
    --stage-light: #9a9a9a;
    --band-top: #f7941d;
    --band-bottom: #e8461e;
    --white: #ffffff;
    --card-dark: #2f2724;
    --card-mid: #4a403c;
    --name-blue: #7fb3c8;
    --text-grey: #c9c2bd;
    --dots: #a89f99;
    --script-grey: #9d9691;
  }
  * { margin: 0; padding: 0; box-sizing: border-box; }
  html, body { width: 1200px; height: 900px; overflow: hidden; }
  body {
    background: radial-gradient(ellipse at 50% 45%, var(--stage-light), var(--stage) 75%);
    position: relative;
  }
  .card {
    position: absolute;
    left: 250px;
    width: 700px;
    height: 400px;
    overflow: hidden;
    box-shadow: 0 10px 24px rgba(0,0,0,.35);
  }
  /* Front */
  .card-front { top: 40px; }
  .front-photo {
    position: absolute; inset: 0;
    background: linear-gradient(180deg, #f4f4f2 0%, #e9e7e3 16%, #b39c80 34%, #8f7660 52%, #5d7a3c 64%, #4f7a2e 100%);
  }
  .brand-band {
    position: absolute; left: 0; right: 0; top: 262px; height: 76px;
    background: linear-gradient(180deg, var(--band-top), var(--band-bottom));
    display: flex; align-items: center; justify-content: center;
  }
  .brand-name {
    font-family: "Open Sans", sans-serif; font-weight: 700;
    font-size: 34px; color: var(--white); letter-spacing: .5px;
  }
  /* Back */
  .card-back {
    top: 470px;
    background: linear-gradient(120deg, var(--card-dark) 0%, var(--card-mid) 55%, var(--card-dark) 100%);
  }
  .agent-photo {
    position: absolute; left: 110px; top: 0; width: 270px; height: 400px;
    background: radial-gradient(ellipse 60% 45% at 50% 28%, #b98463 0%, #8a5a3c 45%, rgba(40,32,30,0) 100%),
                linear-gradient(180deg, #3a302c 0%, #1f1a19 100%);
  }
  .monogram {
    position: absolute; left: 34px; top: 150px;
    font-family: "Cabin", sans-serif; font-weight: 400; font-size: 40px;
    color: var(--name-blue); letter-spacing: 2px;
  }
  .details {
    position: absolute; left: 410px; top: 40px; width: 270px;
    font-family: "Cabin", sans-serif; font-weight: 400; color: var(--text-grey);
  }
  .agent-name {
    font-size: 25px; font-weight: 400; color: var(--name-blue);
    letter-spacing: 1px; line-height: 1; white-space: nowrap;
  }
  .agent-title { font-size: 14px; letter-spacing: 4px; margin-top: 5px; }
  .rule { border-top: 2px dotted var(--dots); margin: 9px 0; }
  .contact-row {
    display: flex; align-items: center; gap: 10px;
    font-size: 13.5px; line-height: 22px; white-space: nowrap;
  }
  .contact-row svg { width: 15px; height: 15px; flex: none; }
  .address { font-size: 13.5px; line-height: 19px; white-space: nowrap; }
  .address + .address { margin-top: 2px; }
  .slogan {
    position: absolute; right: 40px; bottom: 40px;
    font-family: "Allura", cursive; font-size: 36px; color: var(--script-grey);
    white-space: nowrap;
  }
</style>
</head>
<body>
  <section class="card card-front">
    <div class="front-photo" role="img" aria-label="Photograph of a large two-storey suburban home with a green lawn"></div>
    <div class="brand-band"><span class="brand-name">Bright Lantern Realty</span></div>
  </section>

  <section class="card card-back">
    <div class="agent-photo" role="img" aria-label="Portrait photograph of the agent, Gloria Penwick"></div>
    <div class="monogram">GP</div>
    <div class="details">
      <h1 class="agent-name">GLORIA PENWICK</h1>
      <p class="agent-title">BROKER ASSOCIATE</p>
      <div class="rule"></div>
      <p class="contact-row">
        <svg viewBox="0 0 16 16" fill="var(--text-grey)"><path d="M3 1l3 3-1.5 2a9 9 0 0 0 5.5 5.5L12 10l3 3-2 2C7 15 1 9 1 3z"/></svg>
        : 727-481-6054
      </p>
      <p class="contact-row">
        <svg viewBox="0 0 16 16" fill="none" stroke="var(--text-grey)" stroke-width="1.4"><rect x="1" y="3" width="14" height="10"/><path d="M1 3l7 6 7-6"/></svg>
        : hereisgloria@maplenest.example
      </p>
      <p class="contact-row">
        <svg viewBox="0 0 16 16" fill="none" stroke="var(--text-grey)" stroke-width="1.2"><circle cx="8" cy="8" r="6.5"/><ellipse cx="8" cy="8" rx="3" ry="6.5"/><path d="M1.5 8h13M2.5 5h11M2.5 11h11"/></svg>
        : listedbygloria.example
      </p>
      <div class="rule"></div>
      <p class="address">48217 Orrington Blvd Ste 101, Tampa,<br>FL 30918</p>
      <p class="address">2948 Velo Ct Ste 101, New Port Richey,<br>FL 30742</p>
    </div>
    <p class="slogan">Every key opens a new chapter</p>
  </section>
</body>
</html>
```